Real Estate business card for me

Business card for a realtor. I have just a few "must haves"... so I am hoping to get some great ideas back without my telling you what I want.

I just want something cool, appealing to the eye, modern-ish while still looking clean and professional. I'm a young-spirited 40 yo man. I don't wan the business card of a 23 year old or a 63 year old! haha

Industry/Entity Type

Real Estate Agent

Contact Information for Business Card

Whatever Wexford Callaway logo you use, it should be true WC purple color. Outside of that, color scheme is open to ideas.

Requirements
Must have
• Must include:
• Wexford Callaway, Morrow Estates
• Dale Fensworth
• HOMEAGENTĀ®
• 604.771.3948
• HomesWithDale@mailnest.example
Nice to have
• Can include my picture, but it doesn't have to. I saw a card the other day with a house sketch on the backside saying "Your referrals are the sincerest compliment I can receive". That was cool. I also saw a card which one side was just a full frame picture of me, info on reverse side. I like all those ideas as well, but definitely open to ANYTHING cool, a little different, stands out from the monotony of business cards realtors are passing around. It needs to have a Wexford logo on it somewhere, but I don't want it huge or the focal point. Im selling me, not the franchise. You can literally google Wexford Callaway Home Services and find all of the logos. Any of the main stream ones will work. They are typically a dark purple or dark purple and cream.
Should not have
• I do not want a huge logo presence.

```html
<!DOCTYPE html>
<html lang="en">
<head>
<meta charset="utf-8">
<title>Dale Fensworth – Business Card</title>
<link href="https://fonts.googleapis.com/css2?family=Arimo:wght@400;700&display=swap" rel="stylesheet">
<style>
  :root {
    --bg: #ecebe8;
    --purple-deep: #2a0635;
    --purple-mid: #5a1a6a;
    --purple-glow: #8e3f96;
    --gold: #d9922a;
    --white: #ffffff;
    --lavender: #d9c7de;
  }
  html, body {
    margin: 0;
    width: 1200px;
    height: 1200px;
    overflow: hidden;
    background: var(--bg);
    font-family: "Arimo", Arial, sans-serif;
  }
  .card {
    position: absolute;
    left: 130px;
    width: 940px;
    height: 537px;
    overflow: hidden;
    background: radial-gradient(ellipse 55% 60% at 50% 52%, var(--purple-glow) 0%, var(--purple-mid) 45%, var(--purple-deep) 100%);
    box-shadow: 0 10px 24px rgba(0,0,0,0.22);
  }
  .card-front { top: 42px; }
  .card-back { top: 621px; }
  .gold-band {
    position: absolute;
    left: 0; right: 0; bottom: 0;
    height: 62px;
    background: var(--gold);
  }
  .portrait {
    position: absolute;
    left: 90px;
    bottom: 62px;
    width: 420px;
    height: 420px;
    border-radius: 46% 46% 0 0 / 40% 40% 0 0;
    background: linear-gradient(180deg, #b98a6c 0%, #9c6f55 38%, #2b2b30 60%, #1b1b1f 100%);
  }
  .name-block {
    position: absolute;
    line-height: 0.9;
    letter-spacing: -1px;
  }
  .name-first { color: var(--gold); display: block; }
  .name-last { color: var(--white); display: block; }
  .title {
    display: block;
    color: var(--white);
    text-align: right;
    letter-spacing: 0.5px;
  }
  .card-front .name-block { left: 470px; top: 175px; font-size: 92px; }
  .card-front .title { font-size: 30px; margin-top: 4px; }
  .card-back .name-block { left: 130px; top: 150px; font-size: 72px; }
  .card-back .title { font-size: 24px; margin-top: 4px; }
  .brand-mark {
    position: absolute;
    display: flex;
    align-items: center;
    gap: 12px;
    color: var(--white);
  }
  .brand-dot {
    flex: none;
    border: 2px solid var(--white);
    border-radius: 50%;
  }
  .card-front .brand-mark { right: 60px; top: 60px; font-size: 18px; }
  .card-front .brand-dot { width: 26px; height: 26px; }
  .card-back .brand-mark { left: 525px; top: 68px; font-size: 27px; line-height: 1.3; }
  .card-back .brand-dot { width: 70px; height: 70px; border-color: var(--lavender); }
  .contact {
    position: absolute;
    left: 520px;
    top: 345px;
    color: var(--white);
    font-size: 23px;
  }
  .contact-row {
    display: flex;
    align-items: center;
    gap: 14px;
    margin-bottom: 14px;
  }
  .contact-row svg { width: 26px; height: 26px; flex: none; }
</style>
</head>
<body>

<section class="card card-front">
  <div class="brand-mark">
    <span class="brand-dot"></span>
    <span>Wexford Callaway</span>
  </div>
  <div class="portrait" role="img" aria-label="Portrait photo of the agent in a dark blazer and white shirt"></div>
  <div class="name-block">
    <span class="name-first">dale</span>
    <span class="name-last">fensworth</span>
    <span class="title">HOMEAGENT®</span>
  </div>
  <div class="gold-band"></div>
</section>

<section class="card card-back">
  <div class="name-block">
    <span class="name-first">dale</span>
    <span class="name-last">fensworth</span>
    <span class="title">HOMEAGENT®</span>
  </div>
  <div class="brand-mark">
    <span class="brand-dot"></span>
    <span>Wexford Callaway<br>Morrow Estates</span>
  </div>
  <div class="contact">
    <div class="contact-row">
      <svg viewBox="0 0 24 24" fill="none" stroke="#fff" stroke-width="1.6"><rect x="6" y="2" width="12" height="20" rx="2"/><line x1="10" y1="18.5" x2="14" y2="18.5"/></svg>
      <span>604.771.3948</span>
    </div>
    <div class="contact-row">
      <svg viewBox="0 0 24 24" fill="none" stroke="#fff" stroke-width="1.6"><rect x="2" y="5" width="20" height="14"/><polyline points="2,5 12,13 22,5"/><line x1="2" y1="19" x2="9" y2="11"/><line x1="22" y1="19" x2="15" y2="11"/></svg>
      <span>HomesWithDale@mailnest.example</span>
    </div>
  </div>
  <div class="gold-band"></div>
</section>

</body>
</html>
```